Dalton Power Supply, Inc. Business Card Design

We are an Electrical Distributor looking for a Modern, Professional Business Card design.

Target Market(s)

Residential Commercial Industrial

Industry/Entity Type

Electrical

Contact Information for Business Card

Dalton Power Supply, Inc.
418 Maple Ridge Lane
Brookvale, NC 27514
555-214-7630
555-214-8842 Fax
daltonpower@brightmail-example.net

```html
<!DOCTYPE html>
<html lang="en">
<head>
<meta charset="utf-8">
<title>Dalton Power Supply, Inc. — Business Card</title>
<link href="https://fonts.googleapis.com/css2?family=Roboto+Condensed:wght@300;700&display=swap" rel="stylesheet">
<style>
  :root {
    --backdrop: #e9e9e7;
    --paper: #f1f1ef;
    --brand-green: #0f5e3a;
    --leaf-green: #a9c46a;
    --wordmark-green: #93b24f;
    --ink-white: #ffffff;
    --font-main: "Roboto Condensed", "Arial Narrow", sans-serif;
  }
  * { box-sizing: border-box; margin: 0; padding: 0; }
  html, body {
    width: 1200px; height: 800px; overflow: hidden;
    background: var(--backdrop);
    font-family: var(--font-main);
  }
  .canvas {
    width: 1200px; height: 800px;
    display: flex; align-items: center; justify-content: center;
  }
  .business-card {
    width: 980px; height: 560px;
    border-radius: 44px;
    overflow: hidden;
    display: flex;
    box-shadow: 0 18px 40px rgba(0,0,0,0.18);
  }
  .brand-panel {
    width: 370px;
    background: var(--paper);
    display: flex; flex-direction: column;
    align-items: center; justify-content: center;
    gap: 40px;
    padding: 40px 30px;
  }
  .brand-mark {
    width: 180px; height: 180px; border-radius: 50%;
    background: var(--leaf-green);
    flex: none;
  }
  .brand-name {
    color: var(--wordmark-green);
    font-weight: 700;
    font-size: 46px;
    line-height: 1.02;
    text-align: center;
    text-transform: uppercase;
    letter-spacing: 0.5px;
  }
  .info-panel {
    flex: 1;
    background: var(--brand-green);
    color: var(--ink-white);
    padding: 78px 40px 0 64px;
    display: flex; flex-direction: column;
  }
  .company-address {
    font-style: normal;
    font-weight: 300;
    font-size: 44px;
    line-height: 1.12;
  }
  .contact-list {
    list-style: none;
    margin-top: 90px;
    display: flex; flex-direction: column; gap: 16px;
  }
  .contact-item {
    display: flex; align-items: center; gap: 16px;
    font-weight: 300;
    font-size: 38px;
    line-height: 1;
    white-space: nowrap;
  }
  .contact-item.email { font-size: 32px; }
  .contact-icon {
    width: 46px; height: 46px; border-radius: 50%;
    background: var(--ink-white);
    display: flex; align-items: center; justify-content: center;
    flex: none;
  }
  .contact-icon svg { width: 26px; height: 26px; }
</style>
</head>
<body>
<main class="canvas">
  <article class="business-card">
    <section class="brand-panel">
      <span class="brand-mark"></span>
      <div class="brand-name">Dalton<br>Power Supply</div>
    </section>
    <section class="info-panel">
      <address class="company-address">
        Dalton Power Supply, Inc.<br>
        418 Maple Ridge Lane<br>
        Brookvale, NC 27514
      </address>
      <ul class="contact-list">
        <li class="contact-item phone">
          <span class="contact-icon">
            <svg viewBox="0 0 24 24" aria-hidden="true"><path fill="#0f5e3a" d="M6.6 2.5l3 3.2-1.8 2.4c1 2.3 2.8 4.2 5.1 5.3l2.4-1.8 3.2 3-2 3.2C10.6 17.5 6.4 13.3 4.2 7.5z"/></svg>
          </span>
          555-214-7630
        </li>
        <li class="contact-item fax">
          <span class="contact-icon">
            <svg viewBox="0 0 24 24" aria-hidden="true"><g fill="#0f5e3a"><rect x="4" y="3" width="5" height="18" rx="1"/><rect x="10" y="7" width="10" height="14" rx="1"/></g><g fill="#fff"><rect x="12" y="9" width="6" height="3"/><rect x="12" y="14" width="2" height="2"/><rect x="16" y="14" width="2" height="2"/><rect x="12" y="17" width="2" height="2"/><rect x="16" y="17" width="2" height="2"/></g></svg>
          </span>
          555-214-8842
        </li>
        <li class="contact-item email">
          <span class="contact-icon">
            <svg viewBox="0 0 24 24" aria-hidden="true"><rect x="3" y="6" width="18" height="12" rx="1" fill="#0f5e3a"/><path d="M3.5 6.5L12 13l8.5-6.5" fill="none" stroke="#fff" stroke-width="1.4"/></svg>
          </span>
          daltonpower@brightmail-example.net
        </li>
      </ul>
    </section>
  </article>
</main>
</body>
</html>
```